Give us a remarkable appearance

We need a unique, remarkable stationery design (Business Cards, Business Letters, Email Signature etc.). The design should use our logo.

Verlan-Consulting is a startup in consulting, management and IT services and individual software development for the financial industry.

Verlan in english is agate stone. We would like to see designs that use colors out of the agate stone color range.

Preferred COLORS: gold, dark red (burgundy), white, dark grey, black ** see attached Logos **

The used font should be available for further usage with texts etc.

The design should express: modernity, precious, high quality, lightness, stability, ecological awareness, speedy, reliability, simplicity, sustainability.

Target Market(s)

C-Level and Business Clients, Professionals

Industry/Entity Type

Business

Logo Text

Logo styles of interest
Pictorial/Combination Logo
Abstract Logo
Wordmark Logo
Requirements
Must have
• Business Cards, Business Papers, Email Signature
Nice to have
• Door plate, Flyersheet (basic structure), Envelop...

```html
<!DOCTYPE html>
<html lang="en">
<head>
<meta charset="utf-8">
<title>Verlan Consulting – Stationery</title>
<link rel="stylesheet" href="https://fonts.googleapis.com/css2?family=Exo+2:wght@400;500;600&display=swap">
<style>
  :root {
    --backdrop: #353535;
    --paper: #ffffff;
    --burgundy: #772b2d;
    --charcoal: #3b3b3b;
    --gold: #c99a4c;
    --ink: #2b2b2b;
    --ghost: #f0f0f0;
  }
  * { box-sizing: border-box; margin: 0; padding: 0; }
  html, body { width: 1200px; height: 1200px; overflow: hidden; }
  body {
    background: var(--backdrop);
    font-family: "Exo 2", sans-serif;
    position: relative;
  }
  .sheet {
    position: absolute;
    background: var(--paper);
    box-shadow: 0 8px 18px rgba(0,0,0,.45);
    overflow: hidden;
  }
  .sheet svg.wave { position: absolute; left: 0; bottom: 0; }

  .brand {
    display: flex; align-items: center; gap: 10px;
    color: var(--gold); font-weight: 600; letter-spacing: 3px; white-space: nowrap;
  }
  .brand .dot { flex: none; border-radius: 50%; background: var(--gold); }

  /* Letterhead */
  .letterhead { left: 129px; top: 40px; width: 593px; height: 767px; }
  .letterhead .address {
    position: absolute; left: 30px; top: 20px; font-style: normal;
    font-size: 8.5px; line-height: 12px; color: var(--ink); font-weight: 500;
  }
  .letterhead .address .icon { position: absolute; left: -18px; top: 1px; }
  .letterhead .contacts {
    position: absolute; left: 445px; top: 18px;
    list-style: none; font-size: 8.5px; color: var(--ink); font-weight: 500;
  }
  .letterhead .contacts li { display: flex; align-items: center; gap: 8px; height: 14px; }
  .letterhead .watermark {
    position: absolute; left: 20px; top: 270px;
    display: flex; align-items: center; gap: 30px;
    color: var(--ghost);
  }
  .watermark .dot { width: 110px; height: 110px; border-radius: 50%; background: var(--ghost); }
  .watermark .name { font-size: 64px; font-weight: 600; letter-spacing: 14px; line-height: 1; }
  .letterhead .brand { position: absolute; left: 68px; top: 720px; font-size: 22px; }
  .letterhead .brand .dot { width: 26px; height: 26px; }

  /* Business card front */
  .card-front { left: 89px; top: 869px; width: 470px; height: 265px; }
  .card-front .person { position: absolute; right: 26px; top: 20px; }
  .card-front .person .name { font-size: 20px; color: var(--burgundy); font-weight: 600; line-height: 1; }
  .card-front .person .role { font-size: 17px; color: var(--ink); line-height: 1.1; }
  .card-front .watermark {
    position: absolute; right: 18px; top: 108px; color: var(--ghost);
    font-size: 34px; font-weight: 600; letter-spacing: 10px; line-height: 1;
  }
  .card-front .details { position: absolute; left: 28px; top: 68px; list-style: none; font-size: 11px; color: var(--ink); font-weight: 500; }
  .card-front .details li { display: flex; align-items: flex-start; gap: 12px; margin-bottom: 10px; line-height: 13px; }
  .card-front .details svg { flex: none; margin-top: 1px; }
  .card-front .brand { position: absolute; left: 58px; top: 224px; font-size: 16px; }
  .card-front .brand .dot { width: 17px; height: 17px; }

  /* Business card back */
  .card-back { left: 630px; top: 859px; width: 473px; height: 268px; background: var(--burgundy); }
  .card-back .brand {
    position: absolute; left: 0; right: 0; top: 104px;
    justify-content: center; font-size: 28px; letter-spacing: 3px; gap: 12px;
  }
  .card-back .brand .dot { width: 34px; height: 34px; }
  .card-back .footer-band {
    position: absolute; left: 0; bottom: 0; width: 100%; height: 24px;
    background: var(--charcoal); color: #fff; font-size: 10px; letter-spacing: 1.5px;
    display: flex; align-items: center; justify-content: center;
  }
</style>
</head>
<body>

<section class="sheet letterhead" aria-label="Letterhead">
  <address class="address">
    <svg class="icon" width="12" height="11" viewBox="0 0 12 11"><path d="M6 0 L12 5 H10 V11 H7 V7 H5 V11 H2 V5 H0Z" fill="var(--burgundy)"/></svg>
    1850 Garnet Court<br>22 North Garnet Avenue<br>Fairview, Ohio 430117
  </address>
  <ul class="contacts">
    <li><svg width="11" height="10" viewBox="0 0 11 10"><path d="M1 3 Q5.5 -1 10 3 L8 4 L7 3 H4 L3 4Z M2 5 H9 V10 H2Z" fill="var(--burgundy)"/></svg>555 014 2209</li>
    <li><svg width="11" height="10" viewBox="0 0 11 10"><rect x="2" y="0" width="7" height="4" fill="none" stroke="var(--burgundy)"/><rect x="0" y="4" width="11" height="6" fill="var(--burgundy)"/></svg>555 014 2200</li>
    <li><svg width="11" height="9" viewBox="0 0 11 9"><rect width="11" height="9" fill="var(--burgundy)"/><path d="M0 0 L5.5 5 L11 0" fill="none" stroke="#fff"/></svg>info@verlanconsulting.com</li>
    <li><svg width="11" height="11" viewBox="0 0 11 11"><circle cx="6" cy="5" r="4" fill="none" stroke="var(--burgundy)" stroke-width="1.5"/><path d="M3 8 L0 11" stroke="var(--burgundy)" stroke-width="2"/></svg>www.verlanconsulting.com</li>
  </ul>
  <div class="watermark" aria-hidden="true">
    <span class="dot"></span>
    <span class="name">VERLAN</span>
  </div>
  <svg class="wave" width="593" height="200" viewBox="0 0 593 200" aria-hidden="true">
    <path d="M330 98 C450 135 560 90 593 0 L593 80 C520 135 420 125 330 98Z" fill="var(--charcoal)"/>
    <path d="M0 133 C120 88 230 73 330 98 C410 118 500 122 593 75 L593 200 L0 200Z" fill="var(--burgundy)"/>
    <path d="M0 133 C120 88 230 73 330 98 C410 118 500 122 593 75" fill="none" stroke="#fff" stroke-width="2.5"/>
  </svg>
  <div class="brand"><span class="dot"></span>Verlan Consulting</div>
</section>

<section class="sheet card-front" aria-label="Business card front">
  <div class="watermark" aria-hidden="true">VERLAN</div>
  <div class="person">
    <p class="name">Daniel Mertens</p>
    <p class="role">Director</p>
  </div>
  <ul class="details">
    <li><svg width="18" height="16" viewBox="0 0 12 11"><path d="M6 0 L12 5 H10 V11 H7 V7 H5 V11 H2 V5 H0Z" fill="var(--burgundy)"/></svg><span>1850 Garnet Court<br>22 North Garnet Avenue<br>Fairview, Ohio 430117</span></li>
    <li><svg width="18" height="15" viewBox="0 0 11 10"><path d="M1 3 Q5.5 -1 10 3 L8 4 L7 3 H4 L3 4Z M2 5 H9 V10 H2Z" fill="var(--burgundy)"/></svg>555 014 2209</li>
    <li><svg width="18" height="15" viewBox="0 0 11 10"><rect x="2" y="0" width="7" height="4" fill="none" stroke="var(--burgundy)"/><rect x="0" y="4" width="11" height="6" fill="var(--burgundy)"/></svg>555 014 2200</li>
    <li><svg width="18" height="13" viewBox="0 0 11 9"><rect width="11" height="9" fill="var(--burgundy)"/><path d="M0 0 L5.5 5 L11 0" fill="none" stroke="#fff"/></svg>mertens@verlanconsulting.com</li>
  </ul>
  <svg class="wave" width="470" height="110" viewBox="0 0 470 110" aria-hidden="true">
    <path d="M265 58 C360 80 440 55 470 0 L470 35 C410 85 330 75 265 58Z" fill="var(--charcoal)"/>
    <path d="M0 70 C90 40 180 38 265 58 C340 76 410 72 470 35 L470 110 L0 110Z" fill="var(--burgundy)"/>
    <path d="M0 70 C90 40 180 38 265 58 C340 76 410 72 470 35" fill="none" stroke="#fff" stroke-width="2"/>
  </svg>
  <div class="brand"><span class="dot"></span>Verlan Consulting</div>
</section>

<section class="sheet card-back" aria-label="Business card back">
  <div class="brand"><span class="dot"></span>Verlan Consulting</div>
  <div class="footer-band">www.verlanconsulting.com</div>
</section>

</body>
</html>
```